Veterinary Service Needs Web Design

Pawvine is a website that connects pet owners with veterinarians in their search area. I like clean, modern, but playful themes. Our service will be very similar to www.Mediqara.com, however instead of doctors and human patients, our service is focused on veterinarians and pet owners/pets. If you are struggling to understand my idea, please visit www.mediqara.com and look how they organize the website. I would like something similar, yet unique, for Pawvine. I have included the png file for the Pawvine logo to this design request.

Home Page:
the home page must include a sign up button for pet owners to create an account, or to log in if they already have account. It must also include a search bar that will allow the user to search for veterinarians via company name, city/state, or zip code, and pick the date of when they would like to book an appointment.

Sign up/Log in Page:
I will need buttons that show an option to log in via Chatterly, or create an account with an email and password. If they are already a member, there should be a button that allows them to log in directly without having to register a new account.

Registration Page: I will need a form that captures the Pet Owner's first and last name, email address (this will also act as user name), password set up, phone number, home address, their pet's name, the breed of the pet, and the pet's birthday (month/year). There should be a button to 'replicate the form' if there is more than one pet they wish to tie to the account.

My Account Page: This page will show all appointments requested and all appointments confirmed. There will also need to be a button that allows the user to cancel the appointment. This page will also display all the information they entered when registering their account and will need a button that allows the user to edit their information.

Results Page:
This will be the page that displays the results of the veterinarians based on the input into the search bar from the home page. There will need to be a filter button that when clicked will bring up options to filter by appointment date request, distance, pet breed served, rating, and next available appointment. Each veterinarian displayed in the results list will need to have their company name, address, distance to user, rating, and a 'Select this veterinarian' button.

Selected Veterinarian from Results Page:
This page will be for when a pet owners clicks the veterinarian of their choice from the Results Page. This page will need to display all the information about that veterinarian - profile image, reviews/rating, address, distance to pet owner, along with all available time slots available for the date originally put into the search bar from the home page.

Veterinarian Log in/Sign up Page:
I will need the veterinarians to have a log in/sign up page. they will need to be able to sign up via email and set a password, or be able to log in directly if they already have an account.

Veterinarian Dashboard:
The veterinarian will need a dashboard which will display a calendar with all of their appointment requests. They will need to be able to click each appointment and click 'confirm' or 'deny'.

Closing Comments:
If you can think of any better UI/UX capabilities/ideas to improve efficiency and appeal, or any extra design ideas that would be appealing to the user, please incorporate this into your design proposals.

I completely understand this is web design and not a fully functioning website. I am asking the winning design to be coded with HTML/CSS, but fully understand it will not be fully functioning until it is coded by a full stack engineer.

Target Market(s)

Pet Owners and Veterinarians

Industry/Entity Type

Veterinary

Coding

Coded - Design and coding required

Number of Pages Required

5+ page

Colors
0054AA
0677BA
7BADD7
CADEEF
E8F1F8
0094D4
00A9DD
6FCCEA
C7EBF8
E9F6FB

Requirements
Must have
• Listed in the design brief.

```html
<!DOCTYPE html>
<html lang="en">
<head>
<meta charset="utf-8">
<title>Pawvine – Find and book a vet</title>
<link href="https://fonts.googleapis.com/css2?family=Montserrat:wght@400;500;600;700;800&family=Open+Sans:wght@400;600&display=swap" rel="stylesheet">
<style>
:root{
  --brand:#0054AA;
  --navy:#0a3d98;
  --navy-deep:#07338a;
  --cyan:#0094D4;
  --icon:#1b7fd2;
  --btn:#0677BA;
  --ink:#1b1b1b;
  --muted:#444;
  --soft:#f5f2f2;
  --green:#7cc242;
  --footer:#1b1b1b;
  --line:#c9c9c9;
}
*{box-sizing:border-box;margin:0;padding:0}
html,body{width:1200px;height:3554px;overflow:hidden}
body{position:relative;font-family:"Montserrat",sans-serif;color:var(--ink);background:#fff}

/* hero */
.hero{position:absolute;left:0;top:0;width:1200px;height:604px;background:linear-gradient(180deg,#8ea9bd 0%,#a7bfcf 55%,#8aa3b6 100%);overflow:hidden}
.hero-photo{position:absolute;left:680px;top:105px;width:280px;height:499px;border-radius:120px 120px 0 0;background:linear-gradient(180deg,#e9eef1 0%,#f6f7f7 60%,#dfe5e9 100%)}
.logo{position:absolute;display:flex;align-items:center;gap:8px}
.logo-name{font-weight:800;color:var(--brand);letter-spacing:-1px}
.logo-dot{border-radius:50%;background:var(--brand)}
.nav{position:absolute;top:39px;left:0;width:1200px;height:20px}
.nav a{position:absolute;color:#fff;font-size:14.5px;font-weight:600;text-decoration:none}
.nav .btn-out{position:absolute;top:-6px;height:33px;border:2px solid #fff;border-radius:6px;color:#fff;font-size:14.5px;font-weight:600;display:flex;align-items:center;justify-content:center}
.hero h1{position:absolute;left:131px;top:224px;color:#fff;font-size:37px;font-weight:800;letter-spacing:.5px}
.hero p{position:absolute;left:131px;top:286px;color:#fff;font-size:18px;line-height:31px;width:420px}
.search{position:absolute;left:131px;top:405px;width:593px;height:65px;background:#fff;display:flex;font-size:13px}
.search .field{display:flex;align-items:center;padding-left:22px;border-right:1px solid #ddd;height:100%}
.search .caret{margin-left:auto;margin-right:24px;width:0;height:0;border-left:5px solid transparent;border-right:5px solid transparent;border-top:6px solid #222}
.search .go{position:absolute;right:8px;top:15px;width:34px;height:34px;border-radius:50%;background:var(--brand)}

/* section titles */
.sec-title{position:absolute;left:0;width:1200px;text-align:center;font-size:22px;font-weight:700}
.rule{position:absolute;left:583px;width:34px;height:3px;background:var(--brand)}

/* services */
.svc{position:absolute;top:746px;width:178px;height:192px;border:1px solid var(--line);background:#fff}
.svc svg{position:absolute;left:59px;top:43px}
.svc span{position:absolute;left:0;right:0;top:128px;text-align:center;font-size:15px;font-weight:500}
.btn{position:absolute;background:var(--btn);color:#fff;font-weight:600;display:flex;align-items:center;justify-content:center;letter-spacing:.3px}

/* help */
.help{position:absolute;left:0;top:1080px;width:1200px;height:651px;background:var(--navy);overflow:hidden}
.help .sec-title{color:#fff;top:52px}
.help .rule{background:#fff;top:99px}
.help-disc{position:absolute;left:343px;top:195px;width:514px;height:514px;border-radius:50%;background:var(--navy-deep)}
.help-photo{position:absolute;left:420px;top:150px;width:364px;height:501px;border-radius:150px 150px 0 0;background:linear-gradient(180deg,#8a6a55 0%,#c9a58a 22%,#7eb0e6 45%,#5d9ad8 100%)}
.help-icon{position:absolute;width:70px;height:70px;border-radius:50%;background:#1e90dc;display:flex;align-items:center;justify-content:center}
.help-item{position:absolute;color:#fff;width:260px}
.help-item h3{font-size:14px;font-weight:700;letter-spacing:.3px;margin-bottom:8px}
.help-item p{font-size:11.5px;line-height:16.5px}
.help-item.l{text-align:right}

/* reviews */
.reviews{position:absolute;left:0;top:1731px;width:1200px;height:528px;background:var(--soft);overflow:hidden}
.card{position:absolute;top:143px;width:295px;height:280px;background:#fff;overflow:hidden}
.card.fade{opacity:.45}
.card .q{position:absolute;left:28px;top:26px;color:var(--green);font-size:40px;font-weight:800;line-height:40px;font-family:Georgia,serif}
.card p{position:absolute;left:49px;top:58px;width:225px;font-family:"Open Sans",sans-serif;font-size:12.6px;line-height:20px;color:#333}
.card .av{position:absolute;left:46px;top:199px;width:44px;height:44px;border-radius:50%;background:linear-gradient(135deg,#7a6a5e,#c9b3a1)}
.card .nm{position:absolute;left:104px;top:204px;font-size:13px;font-weight:700;color:var(--brand)}
.card .ct{position:absolute;left:104px;top:225px;font-size:11px;color:#444}
.dot{position:absolute;top:470px;width:7px;height:7px;border-radius:50%;background:#c9ccd3}
.dot.on{background:#1e78c8}

/* features */
.feat{position:absolute;top:2344px;width:300px;text-align:center}
.feat svg{display:block;margin:0 auto}
.feat h3{margin-top:38px;font-size:18.5px;font-weight:700;line-height:25px}
.feat p{margin-top:20px;font-size:14.3px;line-height:21px;color:#333}
.feat .btn{position:relative;display:inline-flex;margin-top:20px;height:23px;padding:0 10px;font-size:10px;background:#1f8fd6}

/* provider */
.provider{position:absolute;left:0;top:2728px;width:1200px;height:473px;background:var(--soft)}
.provider h2{position:absolute;left:132px;top:85px;width:380px;font-size:22px;line-height:31px;font-weight:700;white-space:nowrap}
.provider p{position:absolute;left:132px;top:172px;width:325px;font-size:14.3px;line-height:21px;color:#333}
.provider-photo{position:absolute;left:520px;top:47px;width:546px;height:382px;background:linear-gradient(135deg,#6f7f3a 0%,#a8a24a 35%,#d79a52 60%,#7d6a34 100%)}

/* footer */
.footer{position:absolute;left:0;top:3201px;width:1200px;height:353px;background:var(--footer);color:#fff}
.footer h4{position:absolute;top:55px;font-size:12.5px;font-weight:700;letter-spacing:.5px}
.footer .mi{position:absolute;left:480px;font-size:11.5px;letter-spacing:.3px}
.ficon{position:absolute;width:24px;height:24px;border-radius:50%;background:#fff;display:flex;align-items:center;justify-content:center}
.ftxt{position:absolute;font-size:11.5px;line-height:15px}
.footer .divider{position:absolute;left:131px;top:270px;width:936px;height:1px;background:#333}
.footer .copy{position:absolute;left:0;width:1192px;top:312px;text-align:center;font-size:9.5px}
</style>
</head>
<body>

<header class="hero">
  <div class="hero-photo" role="img" aria-label="Photo of a white shepherd dog sitting against a blue-grey backdrop"></div>
  <div class="logo" style="left:131px;top:26px">
    <span class="logo-name" style="font-size:44px">Pawvine</span>
    <span class="logo-dot" style="width:34px;height:34px"></span>
  </div>
  <nav class="nav">
    <a style="left:429px">HOME</a>
    <a style="left:517px">ABOUT US</a>
    <a style="left:636px">SERVICES</a>
    <a style="left:747px">CONTACT US</a>
    <span class="btn-out" style="left:876px;width:76px">LOGIN</span>
    <span class="btn-out" style="left:965px;width:102px">REGISTER</span>
  </nav>
  <h1>WELCOME TO PAWVINE</h1>
  <p>Lorem Ipsum is simply dummy text of the printing and typesetting industry</p>
  <form class="search">
    <div class="field" style="width:214px">Company Name</div>
    <div class="field" style="width:179px;padding-left:26px">City/state<span class="caret"></span></div>
    <div class="field" style="border:0;padding-left:32px">Zip code</div>
    <span class="go"><svg width="34" height="34" viewBox="0 0 34 34"><circle cx="16" cy="16" r="5.5" fill="none" stroke="#fff" stroke-width="2"/><line x1="20" y1="20" x2="23" y2="23" stroke="#fff" stroke-width="2.2" stroke-linecap="round"/></svg></span>
  </form>
</header>

<section>
  <h2 class="sec-title" style="top:662px">OUR SERVICES</h2>
  <div class="rule" style="top:708px"></div>
  <div class="svc" style="left:131px">
    <svg width="60" height="64" viewBox="0 0 60 64"><path d="M30 38C14 26 12 14 20 10c5-2 8 1 10 5 2-4 5-7 10-5 8 4 6 16-10 28z" fill="var(--icon)"/><path d="M4 30c4 0 6 4 10 10l10 8v14H16L4 46z M56 30c-4 0-6 4-10 10l-10 8v14h8l12-16z" fill="var(--icon)"/></svg>
    <span>Primary Care</span>
  </div>
  <div class="svc" style="left:321px">
    <svg width="60" height="64" viewBox="0 0 60 64"><path d="M16 4c6 0 10 4 14 4s8-4 14-4c10 0 14 8 12 18-2 12-6 18-8 30-1 8-8 8-9 0l-3-14c-1-4-5-4-6 0l-3 14c-1 8-8 8-9 0-2-12-6-18-8-30C2 12 6 4 16 4z" fill="var(--icon)"/><path d="M16 12v10M11 17h10" stroke="#fff" stroke-width="2.4"/></svg>
    <span>Dentist</span>
  </div>
  <div class="svc" style="left:512px">
    <svg width="64" height="64" viewBox="0 0 64 64" fill="none" stroke="var(--icon)" stroke-width="3"><path d="M20 6l8 5v9l-8 5-8-5v-9z"/><path d="M40 10l8 5v9l-8 5-8-5v-9z"/><path d="M30 28l8 5v9l-8 5-8-5v-9z"/><path d="M14 34l7 4v8l-7 4-7-4v-8z"/><path d="M48 30l7 4v8l-7 4-7-4v-8z"/></svg>
    <span>Dermatologist</span>
  </div>
  <div class="svc" style="left:700px">
    <svg width="60" height="64" viewBox="0 0 60 64" fill="var(--icon)"><ellipse cx="30" cy="44" rx="13" ry="11"/><ellipse cx="12" cy="26" rx="6" ry="8"/><ellipse cx="48" cy="26" rx="6" ry="8"/><ellipse cx="22" cy="12" rx="6" ry="8"/><ellipse cx="38" cy="12" rx="6" ry="8"/></svg>
    <span>Psychiatrist</span>
  </div>
  <div class="svc" style="left:889px">
    <svg width="60" height="64" viewBox="0 0 60 64" fill="none" stroke="var(--icon)" stroke-width="3.4"><path d="M2 36c8-12 17-17 28-17s20 5 28 17c-8 12-17 17-28 17S10 48 2 36z"/><circle cx="30" cy="36" r="9"/><circle cx="30" cy="36" r="3" fill="var(--icon)"/><path d="M30 4v8M12 9l4 6M48 9l-4 6" stroke-linecap="round"/></svg>
    <span>Eye Doctor</span>
  </div>
  <span class="btn" style="left:512px;top:979px;width:176px;height:43px;font-size:13px;background:var(--cyan)">VIEW ALL SERVICES</span>
</section>

<section class="help">
  <h2 class="sec-title">HOW WE CAN HELP</h2>
  <div class="rule"></div>
  <div class="help-disc"></div>
  <div class="help-photo" role="img" aria-label="Photo of a smiling veterinarian in blue scrubs holding a small terrier"></div>

  <div class="help-item l" style="left:116px;top:208px"><h3>INTERNATIONAL VETS</h3><p>Lorem Ipsum is simply dummy text of<br>the printing and typesetting industry</p></div>
  <div class="help-icon" style="left:398px;top:210px"><svg width="34" height="34" viewBox="0 0 60 64" fill="#fff"><ellipse cx="30" cy="44" rx="13" ry="11"/><ellipse cx="12" cy="26" rx="6" ry="8"/><ellipse cx="48" cy="26" rx="6" ry="8"/><ellipse cx="22" cy="12" rx="6" ry="8"/><ellipse cx="38" cy="12" rx="6" ry="8"/></svg></div>

  <div class="help-item l" style="left:36px;top:355px"><h3>EMERGENCIES</h3><p>Lorem Ipsum is simply dummy text of<br>the printing and typesetting industry</p></div>
  <div class="help-icon" style="left:318px;top:355px"><svg width="36" height="36" viewBox="0 0 60 64"><g fill="#fff"><ellipse cx="30" cy="44" rx="15" ry="13"/><ellipse cx="10" cy="26" rx="6" ry="8"/><ellipse cx="50" cy="26" rx="6" ry="8"/><ellipse cx="22" cy="12" rx="6" ry="8"/><ellipse cx="38" cy="12" rx="6" ry="8"/></g><path d="M30 36v16M22 44h16" stroke="#1e90dc" stroke-width="4"/></svg></div>

  <div class="help-item l" style="left:53px;top:516px"><h3>SUPPORT</h3><p>Lorem Ipsum is simply dummy text of<br>the printing and typesetting industry</p></div>
  <div class="help-icon" style="left:332px;top:512px"><svg width="34" height="34" viewBox="0 0 24 24" fill="#fff"><path d="M6.6 10.8c1.4 2.8 3.8 5.1 6.6 6.6l2.2-2.2c.3-.3.7-.4 1-.2 1.1.4 2.3.6 3.6.6.6 0 1 .4 1 1V20c0 .6-.4 1-1 1C10.6 21 3 13.4 3 4c0-.6.4-1 1-1h3.5c.6 0 1 .4 1 1 0 1.3.2 2.5.6 3.6.1.3 0 .7-.2 1z"/></svg></div>

  <div class="help-item" style="left:826px;top:208px"><h3>LOREM IPSUM</h3><p>Lorem Ipsum is simply dummy text of<br>the printing and typesetting industry</p></div>
  <div class="help-icon" style="left:725px;top:210px"><svg width="34" height="30" viewBox="0 0 34 30"><rect x="2" y="7" width="30" height="21" rx="3" fill="#fff"/><path d="M12 7V3h10v4" fill="none" stroke="#fff" stroke-width="2.5"/><path d="M2 15h30" stroke="#1e90dc" stroke-width="2"/><rect x="14" y="12" width="6" height="6" fill="#fff" stroke="#1e90dc" stroke-width="1.5"/></svg></div>

  <div class="help-item" style="left:892px;top:353px"><h3>LOREM IPSUM</h3><p>Lorem Ipsum is simply dummy text of<br>the printing and typesetting industry</p></div>
  <div class="help-icon" style="left:805px;top:355px"><svg width="36" height="34" viewBox="0 0 36 34" fill="none" stroke="#fff" stroke-width="2.5"><path d="M2 3h20v14H10l-5 5v-5H2z"/><path d="M14 12h20v14h-3v5l-5-5H14z" fill="#1e90dc"/></svg></div>

  <div class="help-item" style="left:877px;top:515px"><h3>LOREM IPSUM</h3><p>Lorem Ipsum is simply dummy text of<br>the printing and typesetting industry</p></div>
  <div class="help-icon" style="left:791px;top:512px"><svg width="38" height="34" viewBox="0 0 38 34" fill="none" stroke="#fff" stroke-width="2.4"><rect x="2" y="3" width="30" height="21" rx="2"/><path d="M12 30h12M18 24v6"/><circle cx="22" cy="12" r="5"/><path d="M26 16l6 6"/><path d="M6 18l5-5 4 3"/></svg></div>
</section>

<section class="reviews">
  <h2 class="sec-title" style="top:52px">REVIEWS</h2>
  <div class="rule" style="top:99px"></div>

  <article class="card fade" style="left:-186px"><span class="q">“</span><p>On the other hand, we denounce with righteous indignation and dislike men who are so beguiled and demoralized by the charms of pleasure of the moment, so blinded by desire.</p></article>
  <article class="card" style="left:132px"><span class="q">“</span><p>On the other hand, we denounce with righteous indignation and dislike men who are so beguiled and demoralized by the charms of pleasure of the moment, so blinded by desire.</p><span class="av" role="img" aria-label="Reviewer portrait"></span><span class="nm">Daniel</span><span class="ct">New York</span></article>
  <article class="card" style="left:452px"><span class="q">“</span><p>On the other hand, we denounce with righteous indignation and dislike men who are so beguiled and demoralized by the charms of pleasure of the moment, so blinded by desire.</p><span class="av" role="img" aria-label="Reviewer portrait"></span><span class="nm">Daniel</span><span class="ct">New York</span></article>
  <article class="card" style="left:771px"><span class="q">“</span><p>On the other hand, we denounce with righteous indignation and dislike men who are so beguiled and demoralized by the charms of pleasure of the moment, so blinded by desire.</p><span class="av" role="img" aria-label="Reviewer portrait"></span><span class="nm">Daniel</span><span class="ct">New York</span></article>
  <article class="card fade" style="left:1084px"><span class="q">“</span><p>On the other hand, we denounce with righteous indignation and dislike men who are so beguiled and demoralized by the charms of pleasure of the moment, so blinded by desire.</p><span class="av" role="img" aria-label="Reviewer portrait"></span><span class="nm">Daniel</span><span class="ct">New York</span></article>

  <span class="dot" style="left:564px"></span>
  <span class="dot" style="left:582px"></span>
  <span class="dot on" style="left:600px"></span>
  <span class="dot" style="left:618px"></span>
  <span class="dot" style="left:633px"></span>
</section>

<section>
  <div class="feat" style="left:116px">
    <svg width="70" height="90" viewBox="0 0 70 90" fill="none" stroke="var(--icon)" stroke-width="3.5"><rect x="4" y="4" width="62" height="82" rx="3"/><path d="M14 22l5 5 9-10M36 22h20M14 42h10v10H14zM36 47h20M14 64h10v10H14zM36 69h20"/></svg>
    <h3>Browse providers who<br>take your insurance</h3>
    <p>On the other hand, we denounce with righteous indignation and dislike men who are so beguiled and demoralized.</p>
    <span class="btn">READ MROE</span>
  </div>
  <div class="feat" style="left:450px">
    <svg width="96" height="90" viewBox="0 0 96 90" fill="none" stroke="var(--icon)" stroke-width="3"><rect x="4" y="4" width="88" height="62" rx="3"/><rect x="12" y="12" width="72" height="46"/><path d="M40 66v12M56 66v12M30 86h36M20 22h6M30 22h6M40 22h6M20 30h26M60 18h16v16H60zM68 22v2M68 26v6"/><path d="M22 46l2 4 4 0-3 3 1 4-4-2-4 2 1-4-3-3 4 0zM42 46l2 4 4 0-3 3 1 4-4-2-4 2 1-4-3-3 4 0zM62 46l2 4 4 0-3 3 1 4-4-2-4 2 1-4-3-3 4 0z" stroke-width="1.5" fill="var(--icon)"/></svg>
    <h3>Read reviews<br>from users</h3>
    <p>On the other hand, we denounce with righteous indignation and dislike men who are so beguiled and demoralized.</p>
    <span class="btn">READ MROE</span>
  </div>
  <div class="feat" style="left:786px">
    <svg width="90" height="90" viewBox="0 0 90 90" fill="none" stroke="var(--icon)" stroke-width="3.5"><rect x="4" y="12" width="82" height="74" rx="4"/><path d="M4 28h82M24 4v16M66 4v16M28 56l12 12 22-24"/></svg>
    <h3>Book an appointment<br>today, online</h3>
    <p>On the other hand, we denounce with righteous indignation and dislike men who are so beguiled and demoralized.</p>
    <span class="btn">SEE AVAILABILITY</span>
  </div>
</section>

<section class="provider">
  <h2>Are you a provider interested<br>in reaching new patients?</h2>
  <p>On the other hand, we denounce with righteous indignation and dislike men who are so beguiled and demoralized. There are many variations of passages of Lorem Ipsum available, but the majority have suffered alteration in some form, by injected humour, or randomised</p>
  <span class="btn" style="left:132px;top:324px;width:134px;height:40px;font-size:15px;background:#1f8fd6">READ MORE</span>
  <div class="provider-photo" role="img" aria-label="Photo of a young woman hugging a beagle on the grass in an autumn park"></div>
</section>

<footer class="footer">
  <div class="logo" style="left:131px;top:110px">
    <span class="logo-name" style="font-size:56px">Pawvine</span>
    <span class="logo-dot" style="width:44px;height:44px"></span>
  </div>

  <h4 style="left:480px">MENU</h4>
  <span class="mi" style="top:91px">HOME</span>
  <span class="mi" style="top:110px">ABOUT US</span>
  <span class="mi" style="top:130px">SERVICES</span>
  <span class="mi" style="top:149px">CONTACT US</span>

  <h4 style="left:670px">CONTACT US</h4>
  <span class="ficon" style="left:667px;top:93px"><svg width="12" height="12" viewBox="0 0 24 24"><path d="M12 2a7 7 0 0 0-7 7c0 5 7 13 7 13s7-8 7-13a7 7 0 0 0-7-7zm0 9.5A2.5 2.5 0 1 1 12 6.5a2.5 2.5 0 0 1 0 5z" fill="#1b1b1b"/></svg></span>
  <span class="ftxt" style="left:701px;top:91px">2750 Maple Ridge Road<br>Fairbrook, CA 90210</span>
  <span class="ficon" style="left:667px;top:144px"><svg width="12" height="12" viewBox="0 0 24 24"><path d="M6.6 10.8c1.4 2.8 3.8 5.1 6.6 6.6l2.2-2.2c.3-.3.7-.4 1-.2 1.1.4 2.3.6 3.6.6.6 0 1 .4 1 1V20c0 .6-.4 1-1 1C10.6 21 3 13.4 3 4c0-.6.4-1 1-1h3.5c.6 0 1 .4 1 1 0 1.3.2 2.5.6 3.6.1.3 0 .7-.2 1z" fill="#1b1b1b"/></svg></span>
  <span class="ftxt" style="left:701px;top:141px">Call Us<br>0400 555 019</span>
  <span class="ficon" style="left:667px;top:195px"><svg width="12" height="12" viewBox="0 0 24 24"><path d="M3 5h18v14H3z" fill="#1b1b1b"/><path d="M3 5l9 7 9-7" fill="none" stroke="#fff" stroke-width="1.8"/></svg></span>
  <span class="ftxt" style="left:701px;top:193px">E mail Us<br>info@pawvine.com</span>

  <h4 style="left:961px">FOLLOW US</h4>
  <span class="ficon" style="left:960px;top:93px"></span>
  <span class="ftxt" style="left:996px;top:91px">Like us on<br>CHATTERLY</span>
  <span class="ficon" style="left:960px;top:144px"></span>
  <span class="ftxt" style="left:996px;top:141px">Follow us on<br>CHIRPLINE</span>
  <span class="ficon" style="left:960px;top:195px"></span>
  <span class="ftxt" style="left:996px;top:193px">Follow us on<br>WORKNET</span>

  <div class="divider"></div>
  <p class="copy">Copyright © 2021 All Rights Reserved</p>
</footer>

</body>
</html>
```